Harlune Painting

Need business card design

Target Market(s)

Paint

Industry/Entity Type

Painting

Requirements
Must have
• Brice Halvorn | Superviser
| HarLune Painting
| mobile: (360) 555-0148
| email: Brice@harluneinc.example
| site: www.harluneinc.example
| address: 718 Corliss Rd NE Ste 300, Olympia, WA 98501

```html
<!DOCTYPE html>
<html lang="en">
<head>
<meta charset="utf-8">
<title>HarLune Painting – Business Card</title>
<link rel="stylesheet" href="https://fonts.googleapis.com/css2?family=Libre+Baskerville:wght@700&family=Poppins:wght@400;500;600&display=swap">
<style>
  :root {
    --page-bg: #e9ebee;
    --brand-green: #5fbf24;
    --brand-blue: #1b3a8a;
    --card-white: #ffffff;
    --text-blue: #1d3f8f;
    --rule-green: #7cc84a;
  }
  * { box-sizing: border-box; margin: 0; padding: 0; }
  html, body { width: 1200px; height: 880px; overflow: hidden; }
  body {
    background: var(--page-bg);
    font-family: "Poppins", sans-serif;
    display: flex;
    flex-direction: column;
    align-items: center;
    justify-content: center;
    gap: 32px;
  }
  .card {
    width: 700px;
    height: 400px;
    border-radius: 22px;
    position: relative;
    box-shadow: 0 10px 26px rgba(0,0,0,0.18);
    overflow: hidden;
  }
  .card--back {
    background: linear-gradient(160deg, var(--brand-green) 0%, #3f8f5a 45%, var(--brand-blue) 85%);
    display: flex;
    flex-direction: column;
    align-items: center;
    justify-content: center;
    gap: 34px;
    color: var(--card-white);
  }
  .brand-name {
    font-family: "Poppins", sans-serif;
    font-weight: 600;
    font-size: 44px;
    letter-spacing: 1px;
    display: flex;
    align-items: center;
    gap: 14px;
  }
  .brand-mark {
    width: 20px; height: 20px; border-radius: 50%;
    background: currentColor;
  }
  .card--back .brand-name { color: var(--card-white); }
  .back-site {
    font-size: 15px;
    letter-spacing: 4px;
  }
  .card--front {
    background: var(--card-white);
    display: flex;
    align-items: center;
  }
  .front-brand {
    width: 360px;
    display: flex;
    justify-content: center;
  }
  .card--front .brand-name {
    color: var(--text-blue);
    font-size: 30px;
  }
  .divider {
    width: 1.5px;
    height: 170px;
    background: var(--rule-green);
  }
  .contact {
    padding-left: 34px;
    color: var(--text-blue);
  }
  .contact__name {
    font-family: "Libre Baskerville", serif;
    font-weight: 700;
    font-size: 22px;
    text-transform: uppercase;
    letter-spacing: 0.5px;
  }
  .contact__title {
    color: var(--brand-green);
    font-size: 15px;
    margin-bottom: 14px;
  }
  .contact__address {
    font-size: 14px;
    line-height: 1.5;
    margin-bottom: 8px;
  }
  .contact__row {
    display: flex;
    align-items: center;
    gap: 10px;
    font-size: 14px;
    line-height: 1.7;
  }
  .contact__icon { width: 18px; height: 18px; flex: none; }
</style>
</head>
<body>
  <section class="card card--back">
    <div class="brand-name"><span class="brand-mark"></span>HarLune Painting</div>
    <div class="back-site">www.harluneinc.example</div>
  </section>

  <section class="card card--front">
    <div class="front-brand">
      <div class="brand-name"><span class="brand-mark"></span>HarLune Painting</div>
    </div>
    <div class="divider"></div>
    <div class="contact">
      <div class="contact__name">Brice Halvorn</div>
      <div class="contact__title">Superviser</div>
      <div class="contact__address">718 Corliss Rd NE Ste 300,<br>Olympia, WA 98501</div>
      <div class="contact__row">
        <svg class="contact__icon" viewBox="0 0 18 18" aria-hidden="true">
          <circle cx="9" cy="9" r="9" fill="#5fbf24"/>
          <rect x="6" y="4" width="6" height="10" rx="1.2" fill="none" stroke="#fff" stroke-width="1.4"/>
        </svg>
        (360) 555-0148
      </div>
      <div class="contact__row">
        <svg class="contact__icon" viewBox="0 0 18 18" aria-hidden="true">
          <circle cx="9" cy="9" r="9" fill="#5fbf24"/>
          <rect x="4.5" y="6" width="9" height="6.5" fill="none" stroke="#fff" stroke-width="1.3"/>
          <polyline points="4.5,6 9,10 13.5,6" fill="none" stroke="#fff" stroke-width="1.3"/>
        </svg>
        Brice@harluneinc.example
      </div>
    </div>
  </section>
</body>
</html>
```